Photography Website

I want a website to promote my photography business. Needs to have a portfolio section, about me section, blog, client log in/ private gallery and a contact/quotation form.

Obviously the aim is to get enquiries and hence to lead people to the quotation or contact details. Also the aim is to showcase my photography to further drive enquiries.

Design and aesthetic appeal is crucial.

You can see my FB page here: http://www.example-social.com/pages/Tamsin-Oakridge-Photography/573920184610375

I do mainly weddings, engagements and family shoots.

I'm looking for a design that is custom and unique - something that does not look like a standard template! As a creative professional, I require a design which has 'character' - some ways I think this can be achieved is by choosing theme colours to base the website on, some consistent motifs, printed background/wall paper...? Whilst I am interested in an 'original' design, I would like to maintain a clear minimalist site layout.

In summary, my website must have a 'bold artistic identity'- whether this is achieved by a contemporary, rustic or classic design is open to suggestion. The homepage example which is attached to this brief may help you understand what I mean. (example_homepage.jpg) - this is only an example and it is not necessary for it to be exactly like this - as experienced web-designers I'm sure you will be able to build upon the example/idea.
Updates

Hi, I realize this project needs a bit more guidance so here goes....

I'm looking for a design that is custom and unique - something that does not look like a standard template! As a creative professional, I require a design which has 'character' - some ways I think this can be achieved is by choosing theme colours to base the website on, some consistent motifs, printed background/wall paper...?  Whilst I am interested in an 'original' design, I would like to maintain a clear minimalist site layout.

In summary, my website must have a 'bold artistic identity'- whether this is achieved by a contemporary, rustic or classic design is open to suggestion.

I hope this helps in giving you a better idea about what I am after....

Best,
Tamsin

Have just seen this - absolutely love it!  Similar designs please :)

www.lucyvantrell.example

Target Market(s)

Young families & young couples in the UK. Often professionals, large budget, trendy individuals.

Industry/Entity Type

Business

Requirements
Must have
• Portfolio section ( divided into: weddings, family, engagement, new born etc.)
about me section
A dedicated blog
client log in/ private gallery
contact/quotation form (easily found on web page)
'artistic identity' (see project overview above for more info)
Clean and clear layout
Based around my logo as attached
Nice to have
• I like soft pastel colours but open to suggestion
Whimsical/ retro/ 'quaint' feel to the design/fonts/color...again, open to all ideas...

www.lucyvantrell.example - this site is brilliant, with a simpler layout and less flash. I like the simple homepage especially.

```html
<!DOCTYPE html>
<html lang="en">
<head>
<meta charset="utf-8">
<title>Tamsin Oakridge Photography</title>
<link rel="stylesheet" href="https://fonts.googleapis.com/css2?family=Lato:wght@300;400&family=Playfair+Display:wght@600&display=swap">
<style>
  :root {
    --brand-blue: #1a72b6;
    --ink: #1c1c1c;
    --muted: #9a9a9a;
    --soft: #c9c9c9;
    --stage: #eeeeee;
    --paper: #ffffff;
    --arrow: #bdbdbd;
    --sepia-dark: #2e2a24;
    --sepia-mid: #7d766b;
    --sepia-light: #c9c3b8;
  }
  * { box-sizing: border-box; margin: 0; padding: 0; }
  html, body {
    width: 1200px;
    height: 900px;
    overflow: hidden;
    background: var(--paper);
  }
  .site {
    position: relative;
    width: 1200px;
    height: 900px;
    font-family: "Lato", "Helvetica Neue", Arial, sans-serif;
  }

  /* Brand */
  .brand {
    position: absolute;
    top: 120px;
    left: 0;
    width: 1200px;
    text-align: center;
  }
  .brand__name {
    font-family: "Playfair Display", "Didot", Georgia, serif;
    font-weight: 600;
    font-size: 52px;
    line-height: 1;
    letter-spacing: 3px;
    color: var(--brand-blue);
    text-transform: uppercase;
  }
  .brand__tagline {
    margin-top: 14px;
    font-size: 21px;
    font-weight: 400;
    letter-spacing: 4px;
    color: var(--muted);
    text-transform: uppercase;
  }

  /* Slideshow */
  .showcase {
    position: absolute;
    left: 29px;
    top: 222px;
    width: 1142px;
    height: 526px;
    background: var(--stage);
  }
  .showcase__photo {
    position: absolute;
    left: 161px;
    top: 0;
    width: 814px;
    height: 526px;
    background:
      radial-gradient(ellipse at 72% 45%, var(--sepia-light) 0%, transparent 45%),
      radial-gradient(ellipse at 20% 30%, var(--sepia-dark) 0%, transparent 50%),
      linear-gradient(135deg, var(--sepia-mid) 0%, var(--sepia-light) 55%, var(--sepia-mid) 100%);
  }
  .showcase__arrow {
    position: absolute;
    top: 233px;
    width: 28px;
    height: 62px;
  }
  .showcase__arrow--prev { left: 56px; }
  .showcase__arrow--next { right: 72px; }

  /* Portfolio categories */
  .categories {
    position: absolute;
    left: 33px;
    top: 776px;
    width: 1134px;
    display: flex;
    justify-content: space-between;
    list-style: none;
    font-size: 23px;
    font-weight: 300;
    color: var(--soft);
    text-transform: uppercase;
    white-space: nowrap;
  }
  .categories__sep { color: var(--soft); }
  .categories__item--active { color: var(--brand-blue); }

  /* Main navigation */
  .main-nav {
    position: absolute;
    left: 29px;
    top: 808px;
    width: 1142px;
    border-top: 2px solid var(--brand-blue);
  }
  .main-nav__list {
    display: flex;
    justify-content: space-between;
    list-style: none;
    height: 56px;
    align-items: stretch;
  }
  .main-nav__item {
    display: flex;
    align-items: center;
    font-size: 36px;
    font-weight: 300;
    color: var(--ink);
    text-transform: uppercase;
    white-space: nowrap;
  }
  .main-nav__item--active {
    background: var(--brand-blue);
    color: var(--paper);
    padding: 0 12px;
  }
</style>
</head>
<body>
<div class="site">
  <header class="brand">
    <div class="brand__name">Tamsin Oakridge</div>
    <div class="brand__tagline">Photography</div>
  </header>

  <section class="showcase">
    <div class="showcase__photo" role="img" aria-label="Sepia family portrait of a young couple holding their newborn baby outdoors beside a large flower"></div>
    <svg class="showcase__arrow showcase__arrow--prev" viewBox="0 0 28 62" aria-label="Previous">
      <polyline points="26,2 2,31 26,60" fill="none" stroke="var(--arrow)" stroke-width="2"/>
    </svg>
    <svg class="showcase__arrow showcase__arrow--next" viewBox="0 0 28 62" aria-label="Next">
      <polyline points="2,2 26,31 2,60" fill="none" stroke="var(--arrow)" stroke-width="2"/>
    </svg>
  </section>

  <ul class="categories">
    <li>Wedding</li><li class="categories__sep">/</li>
    <li>Engagement</li><li class="categories__sep">/</li>
    <li>Family</li><li class="categories__sep">/</li>
    <li>New Born</li><li class="categories__sep">/</li>
    <li class="categories__item--active">Couples</li><li class="categories__sep">/</li>
    <li>Maternity</li><li class="categories__sep">/</li>
    <li>Lifestyle</li><li class="categories__sep">/</li>
    <li>Studio</li>
  </ul>

  <nav class="main-nav">
    <ul class="main-nav__list">
      <li class="main-nav__item">Gallery</li>
      <li class="main-nav__item">Blog</li>
      <li class="main-nav__item">About</li>
      <li class="main-nav__item main-nav__item--active">Services</li>
      <li class="main-nav__item">Raves</li>
      <li class="main-nav__item">Quotes</li>
      <li class="main-nav__item">Client Login</li>
    </ul>
  </nav>
</div>
</body>
</html>
```